Flyer for New Spa Opening

We need a flyer to increase customer's awareness of our new spa located in Yangon, Myanmar, in a middle-upper class shopping mall. A new hotel will be opening above the mall in Dec 2013.
Updates

Have made payment guaranteed.  Need a good flyer. Thanks.

Hi, I have uploaded a Words File for Flyer Text. Thanks!

Dear Designers,

I have setup a 2nd award, there's too many outstanding designs! Thanks so much.

Regards
Marla

Target Market(s)

-Hotel guest who wants to a spa session to relax
-Woman between 18 - 55 years old who have high spending power in a poor country(Myanmar). They like to use "Big Brands" but do not have much variety available in their country.

Industry/Entity Type

Shopping

Requirements
Must have
• Our services include Body Spa, Facial, Nails, Waxing & Foot Reflexology. We use well-known international brands in our spa including Veridelle, KRU, Varnet, Brisola Terrano and MORLU.

Veridelle, the skin care system researched and developed by The Halvern Dermal Academy (HDA), is an international leader in today’s skin care industry.

We are authorized Veridelle skin spa to provide professional facial and retailing Veridelle products.

Include the logo of the brands

Willowmere Spa
add: No 72, Thuka Road, Min Ye Plaza (Level-5) (6187), Kyimyin Township, Yangon
tel: +959 47208613
email: contactus@velmora-unitedgroup.example

Nice to have
• visually nice and relaxing spa pictures.
Should not have
• price

```html
<!DOCTYPE html>
<html lang="en">
<head>
<meta charset="utf-8">
<title>Willowmere Spa – Flyer</title>
<link rel="stylesheet" href="https://fonts.googleapis.com/css2?family=Cinzel:wght@400;600&family=Cormorant+Garamond:ital,wght@1,600;1,700&family=Arimo:ital,wght@0,400;0,700;1,700&display=swap">
<style>
  :root{
    --stage:#4b4b4b;
    --panel-edge:#f4f4f4;
    --orange:#f08a2c;
    --orange-deep:#e0661a;
    --peach:#f7b98a;
    --peach-light:#fbd6b8;
    --wine:#7a1418;
    --wine-bar:#8c1a1d;
    --white:#ffffff;
    --dark:#1d1a12;
    --include:#f29a2e;
    --logo-ink:#3a3a3a;
  }
  *{box-sizing:border-box;margin:0;padding:0}
  html,body{width:1200px;height:1181px;overflow:hidden}
  body{background:var(--stage);position:relative;font-family:"Arimo",Arial,sans-serif}

  .panel{position:absolute;top:84px;width:509px;height:1016px;border:2px solid var(--panel-edge);
    box-shadow:4px 6px 12px rgba(0,0,0,.55);overflow:hidden}
  .panel--front{left:62px;background:linear-gradient(180deg,var(--peach-light) 0%,var(--peach) 40%,var(--orange) 62%,var(--peach-light) 75%)}
  .panel--back{left:633px;background:var(--dark)}

  /* Front */
  .hero-photo{position:absolute;left:0;top:0;width:100%;height:329px;
    background:linear-gradient(160deg,#c98a62 0%,#f0c7a4 45%,#fbe3cf 75%,#f7c69e 100%)}
  .brand-title{position:absolute;top:340px;left:0;width:100%;text-align:center;
    font-family:"Cormorant Garamond",Georgia,serif;font-style:italic;font-weight:700;
    font-size:68px;line-height:76px;color:var(--wine);text-shadow:1px 1px 2px rgba(255,255,255,.4)}
  .title-rule{position:absolute;top:420px;left:30px;width:447px;height:1px;background:rgba(255,255,255,.7)}
  .services{position:absolute;top:453px;left:116px;list-style:none}
  .services li{display:flex;align-items:center;height:39px;
    font-family:"Cinzel",Georgia,serif;font-size:31px;color:var(--white);letter-spacing:.5px;
    text-shadow:1px 1px 2px rgba(120,40,0,.35)}
  .services svg{width:28px;height:28px;margin-right:12px;flex:none}
  .authorized{position:absolute;top:695px;left:30px;width:447px;height:29px;background:var(--white);
    display:flex;align-items:center;justify-content:center;
    font-family:"Cinzel",Georgia,serif;font-size:19px;color:var(--wine);letter-spacing:.5px}
  .petals-photo{position:absolute;left:0;top:730px;width:100%;height:224px;
    background:linear-gradient(180deg,var(--peach-light) 0%,#f4a6a0 35%,#e0485a 70%,#c72035 100%)}
  .front-footer{position:absolute;left:0;top:954px;width:100%;height:58px;background:var(--wine-bar);
    color:var(--white);font-size:12px;padding:10px 10px;line-height:18px}
  .front-footer b{font-weight:700}

  /* Back */
  .menu-bg{position:absolute;left:0;top:0;width:100%;height:718px;
    background:radial-gradient(ellipse at 70% 10%,#5a6a30 0%,#2e3417 35%,#1a170f 75%)}
  .menu-heading{position:absolute;top:42px;left:157px;width:194px;height:47px;
    background:linear-gradient(180deg,#f7a640,var(--orange-deep));border:1px solid #ffd8a0;
    color:var(--white);font-size:28px;font-weight:400;display:flex;align-items:center;justify-content:center}
  .treatment{position:absolute;left:0;width:100%}
  .treatment--day{top:118px;height:162px}
  .treatment--scrub{top:280px;height:103px}
  .treatment--pamper{top:383px;height:135px}
  .treatment--foot{top:518px;height:118px}
  .treatment--traditional{top:636px;height:42px}
  .treatment--swedish{top:678px;height:40px}
  .treatment__bar{height:20px;background:linear-gradient(180deg,#f7a640,var(--orange-deep));
    color:var(--white);font-weight:700;font-size:13px;text-align:center;line-height:20px}
  .treatment__body{padding:6px 44px 0 58px;color:var(--white);font-style:italic;font-weight:700;
    font-size:12px;line-height:15.5px}
  .treatment__body p:first-child{text-indent:10px}
  .treatment__includes{color:var(--include)}
  .candle-photo{position:absolute;left:0;top:718px;width:100%;height:177px;
    background:linear-gradient(90deg,#3a2a1a 0%,#8a6a3a 35%,#c9b24a 65%,#e8d65a 100%)}
  .brand-area{position:absolute;left:0;top:895px;width:100%;height:117px;background:var(--white)}
  .brand-row{position:absolute;left:0;width:100%;display:flex;align-items:center;
    font-family:"Arimo",Arial,sans-serif;font-weight:700;color:var(--logo-ink)}
  .brand-row--top{top:922px;height:30px;font-size:17px;justify-content:center;gap:44px}
  .brand-row--bottom{top:966px;height:30px;font-size:20px;justify-content:center;gap:80px}
</style>
</head>
<body>

<section class="panel panel--front">
  <div class="hero-photo" role="img" aria-label="Photo of a woman relaxing during a back massage"></div>
  <h1 class="brand-title">Willowmere Spa</h1>
  <div class="title-rule"></div>
  <ul class="services">
    <li><svg viewBox="0 0 28 28"><rect x="1" y="1" width="26" height="26" rx="3" fill="#fff"/><path d="M6 14l6 6 10-12" fill="none" stroke="#e0661a" stroke-width="3.5"/></svg>Body Spa</li>
    <li><svg viewBox="0 0 28 28"><rect x="1" y="1" width="26" height="26" rx="3" fill="#fff"/><path d="M6 14l6 6 10-12" fill="none" stroke="#e0661a" stroke-width="3.5"/></svg>Facial</li>
    <li><svg viewBox="0 0 28 28"><rect x="1" y="1" width="26" height="26" rx="3" fill="#fff"/><path d="M6 14l6 6 10-12" fill="none" stroke="#e0661a" stroke-width="3.5"/></svg>Nails</li>
    <li><svg viewBox="0 0 28 28"><rect x="1" y="1" width="26" height="26" rx="3" fill="#fff"/><path d="M6 14l6 6 10-12" fill="none" stroke="#e0661a" stroke-width="3.5"/></svg>Waxing</li>
    <li><svg viewBox="0 0 28 28"><rect x="1" y="1" width="26" height="26" rx="3" fill="#fff"/><path d="M6 14l6 6 10-12" fill="none" stroke="#e0661a" stroke-width="3.5"/></svg>Foot Massage</li>
  </ul>
  <div class="authorized">AUTHORIZED VERIDELLE SKIN SPA</div>
  <div class="petals-photo" role="img" aria-label="Photo of hands with red nails holding rose petals"></div>
  <footer class="front-footer">
    add: No 72, Thuka Road, Min Ye Plaza (Level-5) (6187), Kyimyin Township, Yangon<br>
    <b>tel: +959 47208613</b> &nbsp;|&nbsp; email: contactus@velmora-unitedgroup.example
  </footer>
</section>

<section class="panel panel--back">
  <div class="menu-bg" role="img" aria-label="Dark spa background with soft green leaves"></div>
  <h2 class="menu-heading">Body Spa</h2>
  <article class="treatment treatment--day">
    <div class="treatment__bar">Willowmere Day Spa (2.5hr)</div>
    <div class="treatment__body">
      <p>A luxurious spa experience designed for total relaxation. A delightful body scrub will leave your skin smooth to the touch, followed by a 60min Swedish Aromatherapy massage. The treatment is complete with a body wrap to nourish your skin and your head gently massaged, giving you a profound sense of pleasure and well-being.</p>
      <p class="treatment__includes">Includes: Body Scrub - 60min Swedish Aromatherapy Massage - Body Wrap with Head Massage</p>
    </div>
  </article>
  <article class="treatment treatment--scrub">
    <div class="treatment__bar">Revitalizing Body Scrub (1hr)</div>
    <div class="treatment__body">
      <p>Your skin is polished smooth and soft to the touch followed by a luxurious body cream massaged in to hydrate the newly revealed skin.</p>
      <p class="treatment__includes">Includes: Body Scrub - Light Body Massage</p>
    </div>
  </article>
  <article class="treatment treatment--pamper">
    <div class="treatment__bar">Pampering Body Treatment (1.5hr)</div>
    <div class="treatment__body">
      <p>An all over body treatment begins with a body scrub to exfoliate dead skin, in preparation for a body wrap that restores your skin to youthful condition. Lastly a luxurious body cream is massaged in leaving your skin beautifully radiant.</p>
      <p class="treatment__includes">Includes: Body Scrub - Body Wrap with Head Massage - Light Body Massage</p>
    </div>
  </article>
  <article class="treatment treatment--foot">
    <div class="treatment__bar">Foot Massage (1hr)</div>
    <div class="treatment__body">
      <p>Pamper your foot that has taken you a hundred miles. Following a foot soak and cleaning, we will begin foot massage on your foot reflex zones stimulating body energy and on your muscles to soothe tired heavy legs.</p>
      <p class="treatment__includes">Includes: Foot Soak - Foot Massage</p>
    </div>
  </article>
  <article class="treatment treatment--traditional">
    <div class="treatment__bar">Traditional Body Massage (1.5hr)</div>
  </article>
  <article class="treatment treatment--swedish">
    <div class="treatment__bar">Swedish Aromatherapy Body Massage (1.5hr)</div>
  </article>
  <div class="candle-photo" role="img" aria-label="Photo of lit candles, spa stones and yellow orchids"></div>
  <div class="brand-area"></div>
  <div class="brand-row brand-row--top">
    <span>Varnet</span><span>Brisola Terrano</span><span>MORLU</span>
  </div>
  <div class="brand-row brand-row--bottom">
    <span>Veridelle</span><span>KRU</span>
  </div>
</section>

</body>
</html>
```